Business Card Design

i am looking a business card for a car rental company long with Taxi service also a logo.
Updates

what is the latest with my project

Industry/Entity Type

Business

Contact Information for Business Card

name of the Company is Brenmoor Auto Hire and Cab Services
Address: Harrow Bend Village, St. Aldric's Parish Westmara
Tele# 558-2047/6194852-613-9075
Email: tolvipark@quenmail.net

Font styles to use
Script

```html
<!DOCTYPE html>
<html lang="en">
<head>
<meta charset="utf-8">
<title>Brenmoor Auto Hire and Cab Services – Business Card</title>
<link rel="stylesheet" href="https://fonts.googleapis.com/css2?family=Playball&family=Roboto:wght@400&family=Tinos&display=swap">
<style>
  :root {
    --page-bg: #ecebe9;
    --card-frame: #fbfbf8;
    --card-face: #7f7e7c;
    --text-light: #ffffff;
    --email-ink: #2b2d6e;
    --band-yellow: #e6e21c;
    --band-black: #141408;
    --vehicle-light: #eceded;
    --vehicle-mid: #b9bcbf;
  }
  * { margin: 0; padding: 0; box-sizing: border-box; }
  html, body {
    width: 1200px;
    height: 800px;
    overflow: hidden;
    background: var(--page-bg);
  }
  .canvas {
    position: relative;
    width: 1200px;
    height: 800px;
  }
  .card {
    position: absolute;
    left: 50px;
    top: 55px;
    width: 1100px;
    height: 690px;
    background: var(--card-frame);
    padding: 18px;
  }
  .card-face {
    position: relative;
    width: 100%;
    height: 100%;
    background: var(--card-face);
    overflow: hidden;
  }
  .company-name {
    position: absolute;
    top: 64px;
    left: 0;
    width: 100%;
    padding-left: 20px;
    text-align: center;
    font-family: "Playball", cursive;
    font-weight: 400;
    font-size: 31px;
    color: var(--text-light);
    text-shadow: 2px 2px 2px rgba(0,0,0,0.55);
  }
  .detail {
    position: absolute;
    left: 43px;
    font-family: "Playball", cursive;
    color: var(--text-light);
    text-shadow: 1px 1px 1px rgba(0,0,0,0.4);
  }
  .detail-address { top: 208px; font-size: 29px; }
  .detail-city { top: 304px; font-size: 22px; }
  .detail-city .label { font-size: 29px; }
  .email-line {
    position: absolute;
    left: 43px;
    top: 366px;
    display: flex;
    align-items: center;
    gap: 14px;
    font-family: "Tinos", serif;
    font-size: 27px;
    color: var(--email-ink);
  }
  .phone-block {
    position: absolute;
    left: 440px;
    top: 280px;
    color: var(--text-light);
  }
  .phone-main {
    display: flex;
    align-items: center;
    gap: 8px;
    font-family: "Roboto", sans-serif;
    font-size: 38px;
    line-height: 48px;
  }
  .phone-alt {
    margin: 0 0 0 66px;
    font-family: "Playball", cursive;
    font-size: 26px;
    line-height: 32px;
  }
  .checker-band {
    position: absolute;
    left: 0;
    bottom: 0;
    width: 100%;
    height: 136px;
    background: linear-gradient(180deg, #6b6a3a 0%, var(--band-yellow) 35%, #8f8c1a 60%, var(--band-black) 100%);
  }
  .vehicle-photo {
    position: absolute;
    left: 564px;
    top: 388px;
    width: 490px;
    height: 216px;
    border-radius: 30px 50px 30px 30px;
    clip-path: polygon(0 22%, 20% 8%, 40% 0, 100% 0, 100% 100%, 0 100%);
    background: radial-gradient(ellipse at 45% 40%, var(--vehicle-light) 0%, var(--vehicle-mid) 70%, #5d6063 100%);
  }
</style>
</head>
<body>
<main class="canvas">
  <section class="card">
    <div class="card-face">
      <div class="checker-band" role="img" aria-label="Yellow and black checkered taxi pattern band"></div>

      <h1 class="company-name">Brenmoor Auto Hire and Cab Services</h1>

      <p class="detail detail-address">Address: Harrow Bend Village</p>
      <p class="detail detail-city"><span class="label">City:</span> St. Aldric's Parish Westmara</p>

      <p class="email-line">
        <svg width="40" height="26" viewBox="0 0 40 26" aria-hidden="true">
          <rect x="1" y="1" width="38" height="24" fill="#ffffff" stroke="#cfcfcf" stroke-width="1"/>
          <polyline points="1,1 20,15 39,1" fill="none" stroke="#9a9a9a" stroke-width="1.5"/>
        </svg>
        <span>tolvipark@quenmail.net</span>
      </p>

      <div class="phone-block">
        <p class="phone-main">
          <svg width="40" height="40" viewBox="0 0 40 40" aria-hidden="true">
            <circle cx="20" cy="20" r="17" fill="none" stroke="#ffffff" stroke-width="2.5"/>
            <path d="M14 11c-2 1-3 3-2 6 2 6 6 10 12 12 3 1 5 0 6-2l-4-4-3 2c-3-1-6-4-7-7l2-3z" fill="#ffffff"/>
          </svg>
          <span>: 558-2047/6194</span>
        </p>
        <p class="phone-alt">852-613-9075</p>
      </div>

      <div class="vehicle-photo" role="img" aria-label="Photo of a white compact SUV"></div>
    </div>
  </section>
</main>
</body>
</html>
```